Business Card Design for Training Business

Clear Path Coaching is a new business that delivers training and other services with a focus on topics related to mental health and wellbeing, for example, Mind Care Basics Course, Resilience etc. We have a strong focus on evidence-based psychology and neuroscience. I have a logo which I will upload with the brief, so please consider colours that work well with the logo.
Target Market(s)
Adults, workplaces (particularly government and not-for-profits)
Industry/Entity Type
Business
Contact Information for Business Card
Head Strong TrainingSamantha SellwoodDirector0438 770 bec@clearpathcoaching.com.au.auwww.headstrongtraining.com.au

```html
<!DOCTYPE html>
<html lang="en">
<head>
<meta charset="utf-8">
<title>Clear Path Coaching – Business Card</title>
<link rel="stylesheet" href="https://fonts.googleapis.com/css2?family=Open+Sans:wght@300;400;600&display=swap">
<style>
  :root {
    --teal: #22bcc0;
    --ink: #000000;
    --paper: #ffffff;
    --text: #ffffff;
    --guide: #2a6fa8;
    --pattern: #3a3a3a;
  }
  * { margin: 0; padding: 0; box-sizing: border-box; }
  html, body {
    width: 1200px;
    height: 740px;
    overflow: hidden;
    background: var(--paper);
  }
  .card {
    position: absolute;
    left: 18px;
    top: 18px;
    width: 1166px;
    height: 706px;
    background: var(--ink);
    overflow: hidden;
    font-family: "Open Sans", Arial, sans-serif;
    color: var(--text);
  }
  .card__pattern {
    position: absolute;
    inset: 0;
    background:
      radial-gradient(ellipse at 70% 55%, rgba(70,70,70,0.45) 0%, rgba(0,0,0,0) 60%),
      radial-gradient(ellipse at 25% 30%, rgba(55,55,55,0.35) 0%, rgba(0,0,0,0) 55%);
  }
  .card__band {
    position: absolute;
    left: 0;
    top: 0;
    width: 100%;
    height: 53px;
    background: var(--teal);
  }
  .card__trim {
    position: absolute;
    left: 26px;
    top: 26px;
    width: 1134px;
    height: 665px;
    border: 1px solid var(--guide);
  }
  .brand {
    position: absolute;
    left: 214px;
    top: 172px;
    font-weight: 300;
    font-size: 42px;
    letter-spacing: 5px;
    color: var(--text);
    white-space: nowrap;
  }
  .brand__mark {
    position: absolute;
    left: 810px;
    top: 96px;
    width: 256px;
    height: 256px;
    border: 3px solid var(--teal);
    border-radius: 50%;
  }
  .person {
    position: absolute;
    left: 80px;
    top: 343px;
  }
  .person__name {
    font-weight: 400;
    font-size: 28px;
    letter-spacing: 3px;
    line-height: 1.1;
    text-transform: uppercase;
  }
  .person__role {
    font-weight: 600;
    font-size: 18px;
    letter-spacing: 2.5px;
    line-height: 1.2;
  }
  .contacts {
    position: absolute;
    left: 78px;
    top: 458px;
    list-style: none;
  }
  .contacts__item {
    display: flex;
    align-items: center;
    height: 47px;
    font-size: 28px;
    font-weight: 400;
    white-space: nowrap;
  }
  .contacts__icon {
    width: 32px;
    height: 32px;
    margin-right: 16px;
    flex: none;
  }
</style>
</head>
<body>
  <main class="card">
    <div class="card__pattern" role="img" aria-label="Faint grey geometric line and circle pattern across the background"></div>
    <div class="card__band"></div>
    <div class="card__trim"></div>

    <div class="brand">CLEAR PATH COACHING</div>
    <div class="brand__mark"></div>

    <div class="person">
      <p class="person__name">Rebecca Thornbury</p>
      <p class="person__role">Director</p>
    </div>

    <ul class="contacts">
      <li class="contacts__item">
        <svg class="contacts__icon" viewBox="0 0 32 32" aria-hidden="true">
          <circle cx="16" cy="16" r="16" fill="var(--teal)"/>
          <path d="M11 8.5c1-.6 1.8-.3 2.3.6l1.4 2.6c.4.8.2 1.5-.5 2l-1 .7c.7 1.8 2.1 3.4 3.9 4.4l.8-.9c.6-.6 1.3-.7 2-.3l2.5 1.5c.8.5 1 1.3.4 2.2-1.2 1.8-2.8 2.3-4.7 1.6-4.4-1.7-7.6-5.1-8.9-9.6-.4-1.8.3-3.6 1.8-4.8z" fill="#000"/>
        </svg>
        +353 1 586 2314
      </li>
      <li class="contacts__item">
        <svg class="contacts__icon" viewBox="0 0 32 32" aria-hidden="true">
          <circle cx="16" cy="16" r="16" fill="var(--teal)"/>
          <g fill="none" stroke="#000" stroke-width="1.5">
            <circle cx="16" cy="16" r="9"/>
            <ellipse cx="16" cy="16" rx="4" ry="9"/>
            <line x1="7" y1="16" x2="25" y2="16"/>
            <line x1="8.5" y1="11.5" x2="23.5" y2="11.5"/>
            <line x1="8.5" y1="20.5" x2="23.5" y2="20.5"/>
            <line x1="16" y1="7" x2="16" y2="25"/>
          </g>
        </svg>
        www.clearpathcoaching.com.au
      </li>
      <li class="contacts__item">
        <svg class="contacts__icon" viewBox="0 0 32 32" aria-hidden="true">
          <circle cx="16" cy="16" r="16" fill="var(--teal)"/>
          <rect x="7.5" y="10" width="17" height="12" rx="1" fill="none" stroke="#000" stroke-width="1.6"/>
          <path d="M7.5 10.5l8.5 7 8.5-7M7.5 21.5l6-5.5M24.5 21.5l-6-5.5" fill="none" stroke="#000" stroke-width="1.6"/>
        </svg>
        bec@clearpathcoaching.com.au
      </li>
      <li class="contacts__item">
        <svg class="contacts__icon" viewBox="0 0 32 32" aria-hidden="true">
          <circle cx="16" cy="16" r="16" fill="var(--teal)"/>
          <path d="M16 6.5c-3.6 0-6.3 2.7-6.3 6.2 0 4.5 6.3 12.3 6.3 12.3s6.3-7.8 6.3-12.3c0-3.5-2.7-6.2-6.3-6.2z" fill="#000"/>
          <circle cx="16" cy="12.8" r="2.4" fill="var(--teal)"/>
        </svg>
        27 Harbour Lane, Baker Street, Dublin, D04 K218
      </li>
    </ul>
  </main>
</body>
</html>
```